Real Estate Development Sign

I am trying to get some good graphic design help for a new real estate development project. We need two designs for two separate large billboard-type directionals, also For Sale Signs, and also bandit directional signs. I have a company who have already given it a shot, but I don't like what they have come up with. I need it to have a WOW factor and pop to catch people's eye, but also simple and easy to read. I've attached what they have done so far. I have proofs of what has already been created and I've attached them. I've also attached the logo for the project, but I'm fine with changing the color for the logo to help make the overall signs more cohesive. I want clean, easy to read and eye catching. I will need to be able to pass the designs on to a company to have them printed for the billboards. One of them is 10x12 and the other is 8x10. Time is of the essence - I've spent too much time trying to get this other company to do what I want.
Updates

Project Deadline Extended
Reason: Need more submissions.

I would like to shoot for Black, Red, White and a touch of Yellow for the colors of the signs.

Industry/Entity Type

Graphic Design

```html
<!DOCTYPE html>
<html lang="en">
<head>
<meta charset="utf-8">
<title>Maple Grove at Summit Ridge – Sign Proofs</title>
<link rel="stylesheet" href="https://fonts.googleapis.com/css2?family=Cinzel:wght@400;600&family=Montserrat:wght@700;800&display=swap">
<style>
  :root {
    --canvas: #ffffff;
    --frame: #d4d4d4;
    --label-grey: #b3b3b3;
    --red: #ee1c1c;
    --red-dark: #8c0a0a;
    --black: #0b0b0b;
    --white: #ffffff;
    --silver-light: #eef0f0;
    --silver-mid: #c9cdcd;
    --yellow: #f3e33a;
    --olive: #6b5c12;
    --ink: #1a1a1a;
  }
  html, body {
    margin: 0;
    padding: 0;
    width: 1200px;
    height: 1000px;
    overflow: hidden;
    background: var(--canvas);
  }
  .proof-sheet {
    position: relative;
    width: 1200px;
    height: 1000px;
  }
  .size-label {
    position: absolute;
    top: 130px;
    left: 0;
    width: 1200px;
    text-align: center;
    font-family: "Montserrat", sans-serif;
    font-weight: 800;
    font-size: 38px;
    letter-spacing: 1px;
    color: var(--label-grey);
    margin: 0;
  }
  .sign {
    position: absolute;
    top: 264px;
    width: 483px;
    height: 579px;
    box-sizing: border-box;
    border: 2px solid var(--frame);
    background: var(--white);
  }
  .sign--dark { left: 70px; }
  .sign--photo { left: 654px; }
  .sign svg { display: block; position: absolute; top: -2px; left: -2px; }
  .headline { font-family: "Cinzel", serif; font-weight: 400; fill: var(--white); }
  .headline-by { font-family: "Cinzel", serif; font-weight: 600; fill: var(--white); }
  .project-name { font-family: "Cinzel", serif; font-weight: 600; fill: var(--ink); }
  .phone { font-family: "Montserrat", sans-serif; font-weight: 800; fill: var(--white); }
  .status { font-family: "Montserrat", sans-serif; font-weight: 700; fill: var(--white); }
</style>
</head>
<body>
<main class="proof-sheet">
  <h1 class="size-label">10´X 8´</h1>

  <!-- Black version -->
  <section class="sign sign--dark" aria-label="Sign option, black">
    <svg width="483" height="579" viewBox="0 0 483 579" xmlns="http://www.w3.org/2000/svg">
      <defs>
        <linearGradient id="dk-silver" x1="0" y1="0" x2="1" y2="1">
          <stop offset="0" stop-color="#dfe2e2"/>
          <stop offset="0.45" stop-color="#f4f5f5"/>
          <stop offset="0.7" stop-color="#c8cccc"/>
          <stop offset="1" stop-color="#e8eaea"/>
        </linearGradient>
        <linearGradient id="dk-arrow" x1="0" y1="0" x2="1" y2="0">
          <stop offset="0" stop-color="#7a0606"/>
          <stop offset="0.5" stop-color="#e01414"/>
          <stop offset="1" stop-color="#ff2a2a"/>
        </linearGradient>
        <linearGradient id="dk-header" x1="0" y1="0" x2="1" y2="0">
          <stop offset="0" stop-color="#2a0202"/>
          <stop offset="1" stop-color="#c81010"/>
        </linearGradient>
        <linearGradient id="dk-panel" x1="0" y1="0" x2="1" y2="0">
          <stop offset="0" stop-color="#8f8f8f"/>
          <stop offset="0.5" stop-color="#e9e9e9"/>
          <stop offset="1" stop-color="#ffffff"/>
        </linearGradient>
      </defs>
      <rect class="artboard" x="12" y="14" width="461" height="470" fill="url(#dk-silver)"/>
      <path class="dark-field" d="M88 484 Q210 120 473 20 L473 484 Z" fill="var(--black)"/>
      <g class="accent-stripes" opacity="0.85">
        <polygon points="462,40 473,30 473,484 448,484" fill="var(--olive)"/>
        <polygon points="430,484 470,90 473,90 444,484" fill="#3a1010"/>
      </g>
      <g class="arrow-up">
        <path d="M120 30 L226 142 L176 142 L176 500 L68 500 L68 142 L14 142 Z" fill="var(--white)"/>
        <path d="M120 40 L212 136 L170 136 L170 500 L74 500 L74 136 L28 136 Z" fill="url(#dk-arrow)"/>
      </g>
      <path class="swoosh" d="M12 484 L12 430 Q160 70 473 14 L473 20 Q210 120 88 484 Z" fill="var(--white)"/>
      <path class="swoosh-edge" d="M88 484 Q210 120 473 20" fill="none" stroke="var(--red)" stroke-width="5"/>
      <rect class="headline-box" x="270" y="136" width="160" height="92" fill="url(#dk-header)"/>
      <text class="headline" text-anchor="end" x="416" y="163" font-size="26" letter-spacing="2">CUSTOM</text>
      <text class="headline" text-anchor="end" x="416" y="188" font-size="26" letter-spacing="2">GARDEN</text>
      <text class="headline" text-anchor="end" x="416" y="213" font-size="26" letter-spacing="2">HOMES</text>
      <text class="headline-by" text-anchor="end" x="406" y="223" font-size="7" letter-spacing="1">BY HARLOW HOMES</text>
      <polygon class="name-panel" points="175,274 460,274 445,461 95,461" fill="url(#dk-panel)"/>
      <circle class="name-dot" cx="180" cy="358" r="9" fill="var(--red)"/>
      <text class="project-name" x="198" y="368" font-size="30">Maple Grove</text>
      <text class="project-name" x="198" y="400" font-size="17" letter-spacing="1">at Summit Ridge</text>
      <rect class="contact-band" x="12" y="493" width="461" height="76" fill="var(--red)"/>
      <text class="phone" text-anchor="middle" x="242" y="541" font-size="52" letter-spacing="3">555.014.2368</text>
      <text class="status" text-anchor="middle" x="242" y="564" font-size="20" letter-spacing="14">NOW SELLING</text>
    </svg>
  </section>

  <!-- Photo version -->
  <section class="sign sign--photo" aria-label="Sign option, photo">
    <svg width="483" height="579" viewBox="0 0 483 579" xmlns="http://www.w3.org/2000/svg">
      <defs>
        <linearGradient id="ph-silver" x1="0" y1="0" x2="1" y2="1">
          <stop offset="0" stop-color="#dfe2e2"/>
          <stop offset="0.45" stop-color="#f4f5f5"/>
          <stop offset="0.7" stop-color="#c8cccc"/>
          <stop offset="1" stop-color="#e8eaea"/>
        </linearGradient>
        <linearGradient id="ph-arrow" x1="0" y1="0" x2="1" y2="0">
          <stop offset="0" stop-color="#7a0606"/>
          <stop offset="0.5" stop-color="#e01414"/>
          <stop offset="1" stop-color="#ff2a2a"/>
        </linearGradient>
        <linearGradient id="ph-scene" x1="0" y1="0" x2="0" y2="1">
          <stop offset="0" stop-color="#a8c7e0"/>
          <stop offset="0.3" stop-color="#b0603c"/>
          <stop offset="0.55" stop-color="#d9b48a"/>
          <stop offset="0.8" stop-color="#8fa86a"/>
          <stop offset="1" stop-color="#5f8a3a"/>
        </linearGradient>
        <linearGradient id="ph-panel" x1="0" y1="0" x2="1" y2="0">
          <stop offset="0" stop-color="#ffffff" stop-opacity="0.1"/>
          <stop offset="0.5" stop-color="#ffffff" stop-opacity="0.9"/>
          <stop offset="1" stop-color="#ffffff"/>
        </linearGradient>
      </defs>
      <rect class="artboard" x="12" y="14" width="461" height="470" fill="url(#ph-silver)"/>
      <path class="home-photo" role="img" aria-label="Photo of a two-storey garden home with landscaped front yard" d="M88 484 Q210 120 473 20 L473 484 Z" fill="url(#ph-scene)"/>
      <g class="accent-stripes">
        <polygon points="455,40 473,25 473,484 440,484" fill="var(--yellow)" opacity="0.7"/>
        <polygon points="420,484 468,120 473,120 436,484" fill="var(--red)" opacity="0.4"/>
      </g>
      <g class="arrow-up">
        <path d="M120 30 L226 142 L176 142 L176 500 L68 500 L68 142 L14 142 Z" fill="var(--white)"/>
        <path d="M120 40 L212 136 L170 136 L170 500 L74 500 L74 136 L28 136 Z" fill="url(#ph-arrow)"/>
      </g>
      <path class="swoosh" d="M12 484 L12 430 Q160 70 473 14 L473 20 Q210 120 88 484 Z" fill="var(--white)"/>
      <path class="swoosh-edge" d="M88 484 Q210 120 473 20" fill="none" stroke="var(--red)" stroke-width="5"/>
      <rect class="headline-box" x="270" y="136" width="160" height="92" fill="var(--red)" opacity="0.85"/>
      <text class="headline" text-anchor="end" x="416" y="163" font-size="26" letter-spacing="2">CUSTOM</text>
      <text class="headline" text-anchor="end" x="416" y="188" font-size="26" letter-spacing="2">GARDEN</text>
      <text class="headline" text-anchor="end" x="416" y="213" font-size="26" letter-spacing="2">HOMES</text>
      <text class="headline-by" text-anchor="end" x="406" y="223" font-size="7" letter-spacing="1">BY HARLOW HOMES</text>
      <polygon class="name-panel" points="175,274 460,274 445,461 95,461" fill="url(#ph-panel)"/>
      <circle class="name-dot" cx="180" cy="358" r="9" fill="var(--red)"/>
      <text class="project-name" x="198" y="368" font-size="30">Maple Grove</text>
      <text class="project-name" x="198" y="400" font-size="17" letter-spacing="1">at Summit Ridge</text>
      <rect class="contact-band" x="12" y="493" width="461" height="76" fill="var(--red)"/>
      <text class="phone" text-anchor="middle" x="242" y="541" font-size="52" letter-spacing="3">555.014.2368</text>
      <text class="status" text-anchor="middle" x="242" y="564" font-size="20" letter-spacing="14">NOW SELLING</text>
    </svg>
  </section>
</main>
</body>
</html>
```